K9 Orbit needs a business card designed

We need a business card designed for K9 Orbit, an expansion of K9 Technics Pty Ltd (www.k9technics.com.au)

We provide high quality professional services for the Australian space industry. Our clients include the Southern Stellar Bureau and companies working in the space industry. We identify people with space related skills both locally and internationally who are then contracted by clients to create products and support space launch activities.

Colours to be used:
- Navy blue #000080
- Rocket metallic #8A7F8D
- Platinum #E5E4E2
- Black #000000
- White #FFFFFF

*Front of the card*
I have attached our K9 Orbit logo, which needs to be the main item on the card. The 'Space' text should be placed to the right of the 'K9' part rather than below, similar to the attached K9 Technics card, which this card should match.

If subtext is included, however, it should read ‘Labour Hire • Consultancy • Project Delivery’ rather than the ‘Design • Build • Test • Maintain’ of the K9 Technics card.

A black background (rather than blue background in the K9 Technics card) might be good, with a white pattern as in the K9 Technics card. If colour is used, the logo should be in its standard colours (as provided for the K9 Orbit logo).

*Back of the card*
Include a smaller K9 Orbit logo on the back.

We need the following details for K9 Orbit personnel (as a template for entry):
- Name
- Company Position
- Mobile Number
- Email
- Office Address
- Include the K9 Orbit website: www.k9orbit.com.au

Overall, we'd like to see a design that communicates the adventure of space, professional integrity, and customer service. We look forward to seeing what you can come up with.

Target Market(s)

We provide high quality professional services for the Australian space industry. Our clients include the Southern Stellar Bureau and companies working in the space industry.

Contact Information for Business Card

- Name
- Company Position
- Mobile Number
- Email
- Office Address

Requirements
Must have
• See project description.

```html
<!DOCTYPE html>
<html lang="en">
<head>
<meta charset="utf-8">
<title>K9 Orbit Business Card</title>
<link href="https://fonts.googleapis.com/css2?family=Lato:wght@400;700&display=swap" rel="stylesheet">
<style>
  :root {
    --stage: #2a2a2c;
    --card-purple: #2f1b5f;
    --card-purple-deep: #271650;
    --white: #ffffff;
    --metallic: #8a7f8d;
    --platinum: #e5e4e2;
    --navy-text: #2b1a5a;
  }
  * { box-sizing: border-box; margin: 0; padding: 0; }
  html, body { width: 1200px; height: 1200px; overflow: hidden; }
  body {
    background: var(--stage);
    font-family: "Lato", sans-serif;
    position: relative;
  }
  .card {
    position: absolute;
    left: 190px;
    width: 820px;
    height: 469px;
    border-radius: 22px;
    overflow: hidden;
  }
  .card-front { top: 110px; background: var(--card-purple); }
  .card-back { top: 620px; background: var(--white); }

  .map-area {
    position: absolute;
    left: 250px; top: 40px;
    width: 380px; height: 390px;
    border-radius: 45% 40% 48% 42%;
    background: radial-gradient(ellipse at center, rgba(20,10,50,0.45) 0%, rgba(20,10,50,0.2) 60%, rgba(20,10,50,0) 75%);
  }

  .brand { position: absolute; }
  .brand-row { display: flex; align-items: center; }
  .brand-dot { border-radius: 50%; flex: none; }
  .brand-name {
    font-family: "Lato", sans-serif;
    font-weight: 700;
    white-space: nowrap;
    letter-spacing: 1px;
  }
  .brand-tagline { white-space: nowrap; color: var(--metallic); font-weight: 400; }

  .card-front .brand { left: 190px; top: 185px; }
  .card-front .brand-row { gap: 18px; }
  .card-front .brand-dot { width: 22px; height: 22px; background: var(--white); }
  .card-front .brand-name { color: var(--white); font-size: 66px; line-height: 1; }
  .card-front .brand-tagline { font-size: 16px; letter-spacing: 0.5px; margin-top: 14px; margin-left: 40px; }

  .card-back .brand { left: 45px; top: 38px; }
  .card-back .brand-row { gap: 12px; }
  .card-back .brand-dot { width: 14px; height: 14px; background: var(--navy-text); }
  .card-back .brand-name { color: var(--navy-text); font-size: 40px; line-height: 1; }
  .card-back .brand-tagline { font-size: 12px; margin-top: 8px; margin-left: 26px; }

  .back-band { position: absolute; inset: 0; }

  .person { position: absolute; left: 55px; top: 228px; }
  .person-name { font-size: 34px; color: var(--metallic); }
  .person-name .first { font-weight: 700; }
  .person-role { font-size: 20px; color: var(--white); margin-top: 2px; }

  .contacts { position: absolute; left: 50px; top: 330px; list-style: none; }
  .contacts li {
    display: flex; align-items: center; gap: 12px;
    color: var(--white); font-size: 19px; line-height: 31px;
  }
  .contacts svg { width: 14px; height: 14px; fill: var(--metallic); }

  .address {
    position: absolute; right: 50px; bottom: 40px;
    color: var(--white); font-size: 20px; text-align: right; line-height: 28px;
  }
</style>
</head>
<body>
  <section class="card card-front">
    <div class="map-area" role="img" aria-label="Faint map of Australia behind the name"></div>
    <div class="brand">
      <div class="brand-row">
        <span class="brand-dot"></span>
        <span class="brand-name">K9 Orbit</span>
      </div>
      <p class="brand-tagline">Labour Hire • Consultancy • Project Delivery</p>
    </div>
  </section>

  <section class="card card-back">
    <svg class="back-band" width="820" height="469" viewBox="0 0 820 469" aria-hidden="true">
      <polygon points="0,200 540,280 820,200 820,469 0,469" fill="var(--card-purple-deep)"/>
    </svg>
    <div class="brand">
      <div class="brand-row">
        <span class="brand-dot"></span>
        <span class="brand-name">K9 Orbit</span>
      </div>
      <p class="brand-tagline">Labour Hire • Consultancy • Project Delivery</p>
    </div>
    <div class="person">
      <p class="person-name"><span class="first">Dana</span> Merrow</p>
      <p class="person-role">Managing Director</p>
    </div>
    <ul class="contacts">
      <li><svg viewBox="0 0 16 16"><path d="M4 1l3 3-2 2c1 2 3 4 5 5l2-2 3 3-2 3C7 15 1 9 1 3z"/></svg>+61 x xxxx xxxx</li>
      <li><svg viewBox="0 0 16 16"><path d="M1 3h14v10H1z M1 3l7 6 7-6"/></svg>website@k9orbit.com.au</li>
      <li><svg viewBox="0 0 16 16"><circle cx="8" cy="8" r="7"/></svg>www.k9orbit.com.au</li>
    </ul>
    <p class="address">Level 6, 42 Harbour St<br>Eastbrook VIC 3190</p>
  </section>
</body>
</html>
```